Ridgecrest Balusters Website Redesign

I want a fresh new design for my website. Original website
www.ridgecrestbalusters.example. Will need to add additional photos for winning designer. Please use the basic layout for new design. Looking to get a more modern, functional site to attract new customer and ne bale to highlight past projects. Need it to be easy to navigate and get in touch with me for inquiries.

Target Market(s)

Builders and home owners in WA state

Industry/Entity Type

Building, Construction, Deck building

Coding

Coded - Design and coding required

Number of Pages Required

5+ page

Font styles to use
Sans Serif

Colors
0054AA
0677BA
7BADD7
CADEEF
E8F1F8
0094D4
00A9DD
6FCCEA
C7EBF8
E9F6FB
00AB8E
00BBA5
67D7C9
C6EFE9
E9F9F6
59FF00
82FF00
B8FF75
E3FFCB
F4FFEA

Requirements
Must have
• Will need to add more photos of completed projects
Nice to have
• Fresh take on old website, something modern
Should not have
• Nothing comes to mind

```html
<!DOCTYPE html>
<html lang="en">
<head>
<meta charset="utf-8">
<title>Ridgecrest Balusters</title>
<link href="https://fonts.googleapis.com/css2?family=Outfit:wght@300;400;500;600;700&display=swap" rel="stylesheet">
<style>
:root{
  --blue:#0054AA;
  --blue-mid:#0677BA;
  --sky:#0094D4;
  --teal:#00AB8E;
  --teal-light:#00BBA5;
  --ink:#1a1a1a;
  --text:#333;
  --line:#8a8a8a;
  --white:#fff;
  --black:#000;
  --strip:#e6e6e6;
}
*{box-sizing:border-box;margin:0;padding:0}
html,body{width:1200px;height:4633px;overflow:hidden}
body{position:relative;background:var(--white);font-family:'Outfit',sans-serif;color:var(--ink)}
.abs{position:absolute}
.btn{position:absolute;display:flex;align-items:center;justify-content:center;border-radius:30px;color:var(--white);font-weight:600;background:linear-gradient(90deg,var(--teal),var(--blue-mid))}
.mark{display:inline-block;width:22px;height:22px;background:var(--blue);border-radius:3px;margin-right:12px;vertical-align:-3px}
.sec-title{position:absolute;font-size:25px;font-weight:600;color:var(--ink)}
.photo{position:absolute;overflow:hidden}

/* hero */
.hero-bg{left:0;top:0;width:1200px;height:583px;background:linear-gradient(160deg,#5a5650 0%,#3b3935 40%,#2a2826 70%,#4a4640 100%)}
.nav{left:0;top:0;width:1200px;height:124px;background:rgba(40,40,40,.55)}
.brand{left:58px;top:30px;color:var(--white);font-size:18px;font-weight:600;line-height:1.2;width:140px}
.nav-links{left:234px;top:50px;display:flex;gap:34px;color:var(--white);font-size:18px;font-weight:600}
.nav-cta{left:963px;top:40px;width:178px;height:43px;font-size:16px}
.stars{left:486px;top:234px;display:flex;gap:5px;align-items:center}
.star{width:22px;height:22px;background:var(--teal-light)}
.hero-title{left:0;top:282px;width:1200px;text-align:center;color:var(--white);font-size:46px;font-weight:700;letter-spacing:.5px}
.hero-sub{left:0;top:350px;width:1200px;text-align:center;color:#f0f0f0;font-size:24px;font-weight:300}
.hero-cta{left:444px;top:418px;width:310px;height:54px;font-size:24px}

/* about */
.about-photo{left:58px;top:642px;width:542px;height:456px;border-radius:26px;background:linear-gradient(180deg,#b9cde0 0%,#d9e3ea 30%,#7c8a62 50%,#9a9a93 70%,#6d6f70 100%)}
.slider{left:100px;top:1058px;width:392px;height:8px;border-radius:4px;background:rgba(255,255,255,.7)}
.slider i{position:absolute;left:62px;top:0;width:56px;height:8px;border-radius:4px;background:var(--blue)}
.about-copy{left:633px;top:670px;width:470px}
.about-copy h3{font-size:25px;font-weight:600;margin-bottom:18px}
.about-copy h4{font-size:22px;font-weight:500;margin-bottom:12px}
.about-copy p{font-size:19px;line-height:26px;color:var(--text);font-weight:300}
.about-cta{left:633px;top:1018px;width:159px;height:46px;font-size:19px}

/* why */
.why-title{left:0;top:1156px;width:1200px;text-align:center}
.why-sub{left:0;top:1206px;width:1200px;text-align:center;font-size:22px;line-height:30px;color:var(--text);font-weight:300}
.card{position:absolute;width:517px;height:204px;border-radius:16px;background:var(--white);box-shadow:0 4px 12px rgba(0,0,0,.14)}
.card.active{background:var(--blue);color:var(--white)}
.card .ic{position:absolute;left:26px;top:28px;width:64px;height:64px;border-radius:14px;background:var(--black);display:flex;align-items:center;justify-content:center}
.card.active .ic{background:var(--blue);border:3px solid var(--white)}
.card h5{position:absolute;left:116px;top:26px;width:360px;font-size:22px;font-weight:600;line-height:30px}
.card p{position:absolute;left:116px;width:370px;font-size:15px;line-height:22px;font-weight:300}
.card.active p{color:#e9f1fb}

/* product */
.prod-title{left:58px;top:1784px}
.prod-sub{left:58px;top:1836px;font-size:22px;line-height:30px;color:var(--text);font-weight:300}
.all-cta{left:984px;top:1844px;width:157px;height:44px;font-size:19px}
.tile{position:absolute;top:1923px;width:260px;height:317px;border-radius:10px;overflow:hidden}
.tile .lbl{position:absolute;left:0;top:100px;width:260px;text-align:center;color:var(--white);font-size:27px;font-weight:600;line-height:34px}
.tile .more{position:absolute;left:81px;top:178px;width:98px;height:28px;border-radius:14px;background:var(--white);color:var(--blue);font-size:14px;font-weight:600;display:flex;align-items:center;justify-content:center}

/* gallery */
.gal-title{left:0;top:2296px;width:1200px;text-align:center}
.gal-sub{left:0;top:2346px;width:1200px;text-align:center;font-size:22px;color:var(--text);font-weight:300}
.gal-main{left:119px;top:2412px;width:962px;height:583px;border-radius:22px;background:linear-gradient(180deg,#4a3e35 0%,#6b5a4a 25%,#3a3a3a 55%,#8d8d88 80%,#a8a8a3 100%)}
.strip{left:58px;top:3029px;width:1083px;height:99px;background:var(--strip)}
.thumb{position:absolute;top:3029px;width:149px;height:99px}
.thumb.on{outline:4px solid var(--blue);outline-offset:-4px}

/* cta band */
.band{left:58px;top:3188px;width:1083px;height:198px;background:var(--blue);overflow:hidden}
.band h2{position:absolute;left:0;top:34px;width:1083px;text-align:center;color:var(--white);font-size:30px;font-weight:600;line-height:38px}
.band-cta{position:absolute;left:440px;top:115px;width:202px;height:55px;border-radius:30px;background:var(--white);color:var(--blue);font-size:25px;font-weight:600;display:flex;align-items:center;justify-content:center}

/* quote */
.quote-title{left:58px;top:3444px}
.quote-sub{left:58px;top:3494px;font-size:22px;color:var(--text);font-weight:300}
.field{position:absolute;border:1.5px solid var(--line);background:var(--white);padding:14px 24px;font-size:21px;color:#aaa;font-weight:300}
.submit{left:58px;top:4103px;width:151px;height:44px;font-size:19px}
.quote-photo{left:653px;top:3445px;width:488px;height:702px;border-radius:26px;background:linear-gradient(160deg,#f2f2f0 0%,#d8d6d2 40%,#9c9a96 65%,#6b4a32 100%)}

/* footer */
.footer{left:0;top:4206px;width:1200px;height:427px;background:var(--black);color:var(--white)}
.f-brand{left:58px;top:40px;font-size:18px;font-weight:600;line-height:1.2;width:160px}
.f-tag{left:58px;top:136px;width:320px;font-size:14px;line-height:19px;font-weight:300}
.socials{left:58px;top:254px;display:flex;gap:10px}
.socials span{width:40px;height:40px;border:2px solid var(--white);border-radius:50%}
.f-col h6{font-size:22px;font-weight:600;margin-bottom:22px}
.f-col a{display:block;color:var(--white);text-decoration:none;font-size:17px;font-weight:300;margin-bottom:22px}
.f-col p{font-size:17px;font-weight:300;line-height:22px;margin-bottom:18px}
.copy{left:0;top:350px;width:1200px;text-align:center;font-size:19px;font-weight:300}
</style>
</head>
<body>

<!-- Hero -->
<section class="abs hero-bg" role="img" aria-label="Photo of a modern home with glass deck railings and an exterior staircase"></section>
<header class="abs nav">
  <div class="abs brand">Ridgecrest Balusters</div>
  <nav class="abs nav-links"><span>HOME</span><span>PRODUCT</span><span>ABOUT</span><span>RAILING PROJECT</span><span>REMODEL PROJECT</span></nav>
  <div class="btn nav-cta">
    <svg width="18" height="18" viewBox="0 0 24 24" style="margin-right:10px"><path fill="#fff" d="M6.6 10.8a15.1 15.1 0 0 0 6.6 6.6l2.2-2.2c.3-.3.7-.4 1-.2 1.1.4 2.3.6 3.6.6.6 0 1 .4 1 1V20c0 .6-.4 1-1 1A17 17 0 0 1 3 4c0-.6.4-1 1-1h3.5c.6 0 1 .4 1 1 0 1.3.2 2.5.6 3.6.1.3 0 .7-.2 1z"/></svg>Contact Us
  </div>
</header>
<div class="abs stars"><span class="star"></span><span class="star"></span><span class="star"></span><span class="star"></span><span class="star"></span><span style="width:60px;height:14px;background:rgba(255,255,255,.6);border-radius:3px;margin-left:8px"></span></div>
<h1 class="abs hero-title">LICENSED, INSURED, &amp; BONDED</h1>
<p class="abs hero-sub">Your trusted partner for both residential &amp; commercial railing projects</p>
<div class="btn hero-cta">Explore Our Product</div>

<!-- About -->
<div class="photo about-photo" role="img" aria-label="Photo of a composite deck with cable railing overlooking a valley town"></div>
<div class="abs slider"><i></i></div>
<div class="abs about-copy">
  <h3><span class="mark"></span>About Us</h3>
  <h4>Licensed, Insured &amp; Bonded</h4>
  <p>Founded in 2020, Ridgecrest Balusters specializes in crafting stylish, durable, and climate-resistant railing systems for homes and commercial spaces across Washington State. With premium materials, expert craftsmanship, and exceptional service, we enhance outdoor spaces with custom solutions that prioritize safety and aesthetics. From decks and balconies to commercial projects, we're your trusted partner for railing excellence.</p>
</div>
<div class="btn about-cta">Contact Us</div>

<!-- Why choose -->
<h3 class="sec-title why-title"><span class="mark"></span>Why Choose Ridgecrest Balusters?</h3>
<p class="abs why-sub">At Ridgecrest Balusters, We ensure every project is<br>tailored to your needs and long-lasting reliability</p>

<div class="card active" style="left:58px;top:1301px">
  <div class="ic"><svg width="34" height="30" viewBox="0 0 34 30"><rect x="1" y="1" width="32" height="28" rx="3" fill="none" stroke="#fff" stroke-width="2.5"/><rect x="6" y="7" width="8" height="16" fill="#fff"/><path d="M18 9h10M18 15h10M18 21h10" stroke="#fff" stroke-width="2.5"/></svg></div>
  <h5>Locally Crafted,<br>Regionally Resilient</h5>
  <p style="top:92px">Our railings are built to withstand the Pacific Northwest's toughest weather, using durable, corrosion-resistant materials for long-lasting performance.</p>
</div>
<div class="card" style="left:624px;top:1301px">
  <div class="ic"><svg width="34" height="30" viewBox="0 0 34 30"><rect x="1" y="1" width="32" height="28" rx="3" fill="none" stroke="#fff" stroke-width="2.5"/><rect x="6" y="7" width="8" height="16" fill="#fff"/><path d="M18 9h10M18 15h10M18 21h10" stroke="#fff" stroke-width="2.5"/></svg></div>
  <h5>Custom Solutions<br>for Every Need</h5>
  <p style="top:92px">We design and craft custom railing systems tailored to your space, style, and needs, from intricate designs to sleek, minimal finishes.</p>
</div>
<div class="card" style="left:58px;top:1527px">
  <div class="ic"><svg width="34" height="30" viewBox="0 0 34 30"><rect x="1" y="1" width="32" height="28" rx="3" fill="none" stroke="#fff" stroke-width="2.5"/><rect x="6" y="7" width="8" height="16" fill="#fff"/><path d="M18 9h10M18 15h10M18 21h10" stroke="#fff" stroke-width="2.5"/></svg></div>
  <h5>Expert Installation &amp;<br>Craftsmanship</h5>
  <p style="top:90px">Our craftsmen deliver exceptional quality, and our installers ensure every railing is securely mounted and meets local safety standards.</p>
</div>
<div class="card" style="left:624px;top:1527px">
  <div class="ic"><svg width="34" height="30" viewBox="0 0 34 30"><rect x="1" y="1" width="32" height="28" rx="3" fill="none" stroke="#fff" stroke-width="2.5"/><rect x="6" y="7" width="8" height="16" fill="#fff"/><path d="M18 9h10M18 15h10M18 21h10" stroke="#fff" stroke-width="2.5"/></svg></div>
  <h5>Full-Service Partner</h5>
  <p style="top:62px">From the initial consultation and design process to installation and ongoing maintenance, we are with you every step of the way to ensure your project exceeds expectations.</p>
</div>

<!-- Products -->
<h3 class="sec-title prod-title"><span class="mark"></span>Our Product</h3>
<p class="abs prod-sub">We offer a wide variety of custom and railing<br>systems designed to meet the needs of every project</p>
<div class="btn all-cta">All Product</div>

<div class="tile" style="left:58px;background:linear-gradient(180deg,#6a6a6a,#3a3a3a 60%,#8a8a8a)" role="img" aria-label="Photo of black aluminum railing panel">
  <div class="lbl">Aluminum<br>Railings</div><div class="more">Learn More</div></div>
<div class="tile" style="left:333px;background:linear-gradient(180deg,#5f6e58,#4a5745 50%,#7b7e7a)" role="img" aria-label="Photo of glass railing on a lawn-side deck">
  <div class="lbl">Glass<br>Railings</div><div class="more">Learn More</div></div>
<div class="tile" style="left:608px;background:linear-gradient(180deg,#5c5a52,#3e3a33 55%,#6a5d4c)" role="img" aria-label="Photo of cable railing on a wooden deck">
  <div class="lbl">Cable<br>Railings</div><div class="more">Learn More</div></div>
<div class="tile" style="left:883px;background:linear-gradient(180deg,#a7a7a7,#8f8f8f 50%,#b8b8b8)" role="img" aria-label="Rendering of a custom staircase railing">
  <div class="lbl">Custom<br>Options</div><div class="more">Learn More</div></div>

<!-- Gallery -->
<h3 class="sec-title gal-title"><span class="mark"></span>Gallery</h3>
<p class="abs gal-sub">Take a closer look at our products and projects</p>
<div class="photo gal-main" role="img" aria-label="Photo of a black aluminum railing on a concrete patio beside a grill and dining set"></div>
<svg class="abs" style="left:993px;top:2458px" width="42" height="42" viewBox="0 0 42 42"><circle cx="17" cy="17" r="13" fill="none" stroke="#222" stroke-width="3.5"/><path d="M27 27l12 12M17 11v12M11 17h12" stroke="#222" stroke-width="3.5" stroke-linecap="round"/></svg>
<div class="abs strip"></div>
<div class="thumb on" style="left:124px;background:linear-gradient(180deg,#6b5c4d,#3e3e3e 55%,#9a9a95)" role="img" aria-label="Thumbnail of patio railing"></div>
<div class="thumb" style="left:284px;background:linear-gradient(180deg,#7d8a80,#4a4f4a 55%,#7a7a75)" role="img" aria-label="Thumbnail of deck railing"></div>
<div class="thumb" style="left:444px;background:linear-gradient(180deg,#c9c7c2,#77736c 55%,#57534d)" role="img" aria-label="Thumbnail of exterior stair railing"></div>
<div class="thumb" style="left:604px;background:linear-gradient(180deg,#6f8fb3,#4a4d48 55%,#7a5e46)" role="img" aria-label="Thumbnail of deck railing with lake view"></div>
<div class="thumb" style="left:764px;background:linear-gradient(180deg,#e6e6e3,#a9a6a0 55%,#4c4a46)" role="img" aria-label="Thumbnail of balcony railing on a house"></div>
<div class="thumb" style="left:924px;background:linear-gradient(180deg,#9fb8d4,#5f6a55 55%,#7a5a3e)" role="img" aria-label="Thumbnail of wooden deck with railing"></div>

<!-- CTA band -->
<section class="abs band">
  <svg class="abs" style="left:0;top:0" width="1083" height="198" viewBox="0 0 1083 198">
    <path d="M0 120 C60 95 120 150 180 170 C220 185 250 190 270 198 L0 198Z" fill="#00AB8E"/>
    <path d="M820 0 C850 40 900 70 960 70 C1020 70 1060 110 1083 130 L1083 0Z" fill="#00AB8E"/>
  </svg>
  <h2>Are you interested in<br>Our construction services?</h2>
  <div class="band-cta">Contact Us</div>
</section>

<!-- Quote -->
<h3 class="sec-title quote-title"><span class="mark"></span>Request a Quote</h3>
<p class="abs quote-sub">Make sure to fill in the text box correctly</p>
<div class="field" style="left:58px;top:3558px;width:250px;height:58px">First Name</div>
<div class="field" style="left:320px;top:3558px;width:283px;height:58px">Last Name</div>
<div class="field" style="left:58px;top:3632px;width:545px;height:58px">Email</div>
<div class="field" style="left:58px;top:3708px;width:545px;height:58px">Subject</div>
<div class="field" style="left:58px;top:3783px;width:545px;height:286px;font-size:18px">How can we help you?</div>
<div class="btn submit">Submit</div>
<div class="photo quote-photo" role="img" aria-label="Photo of an interior carpeted staircase with black metal railing"></div>

<!-- Footer -->
<footer class="abs footer">
  <div class="abs f-brand">Ridgecrest Balusters</div>
  <p class="abs f-tag">Your trusted partner for both<br>residential and commercial railing projects</p>
  <div class="abs socials"><span></span><span></span><span></span><span></span></div>
  <div class="abs f-col" style="left:642px;top:48px">
    <h6>Quick Link</h6>
    <a>About Us</a><a>Product</a><a>Project</a><a>Contact</a>
  </div>
  <div class="abs f-col" style="left:874px;top:48px;width:300px">
    <h6>Contact Us</h6>
    <p>4821 Summit View Ln<br>Yakima, WA 98901</p>
    <p>Contact: (555) 014-2290</p>
    <p>Email:<br>info@ridgecrestbalusters.example</p>
  </div>
  <p class="abs copy">Ridgecrest Balusters © 2024 All Rights Reserved</p>
</footer>

</body>
</html>
```